Maison Corvel

I am actually making my own traditional french food.
Everything is homemade with passion.
I make differente terrines, jams, macaroons, rillettes and much more
I do as well cocktail party and catering
Updates

Hello everyone,

On the business card I would like to see appear if it's possible these following informations: traditional french food, cocktail party and catering.

Industry/Entity Type

Catering

```html
<!DOCTYPE html>
<html lang="en">
<head>
<meta charset="utf-8">
<title>Maison Corvel – Business Cards</title>
<link href="https://fonts.googleapis.com/css2?family=Tinos:wght@400;700&family=Italianno&display=swap" rel="stylesheet">
<style>
  :root {
    --backdrop: #7d0a0b;
    --card-white: #ffffff;
    --band-blue: #2e3192;
    --ink: #1a1a1a;
    --accent-red: #d4202f;
    --light-text: #ffffff;
  }
  * { margin: 0; padding: 0; box-sizing: border-box; }
  html, body {
    width: 1200px;
    height: 869px;
    overflow: hidden;
    background: var(--backdrop);
  }
  .canvas {
    width: 1200px;
    height: 869px;
    display: flex;
    align-items: center;
    justify-content: center;
    gap: 44px;
  }
  .card {
    position: relative;
    width: 540px;
    height: 340px;
    border-radius: 26px;
    overflow: hidden;
    background: var(--card-white);
    font-family: "Tinos", "Times New Roman", serif;
    color: var(--ink);
  }
  .band {
    position: absolute;
    left: 0;
    width: 100%;
    background: var(--band-blue);
  }
  .card-front .band-top { top: 0; height: 70px; }
  .card-front .band-bottom { bottom: 0; height: 82px; }
  .card-back .band-bottom { bottom: 0; height: 150px; }

  .brand {
    position: absolute;
    left: 0;
    width: 100%;
    display: flex;
    flex-direction: column;
    align-items: center;
  }
  .card-front .brand { top: 100px; }
  .card-back .brand { top: 52px; }

  .brand-mark {
    display: flex;
    align-items: center;
    gap: 12px;
  }
  .brand-dot {
    width: 22px;
    height: 22px;
    border-radius: 50%;
    background: var(--accent-red);
  }
  .brand-name {
    font-size: 30px;
    font-weight: 400;
    letter-spacing: 1px;
    text-transform: uppercase;
    color: var(--ink);
  }
  .tagline {
    margin-top: 14px;
    font-family: "Italianno", "Brush Script MT", cursive;
    font-size: 38px;
    line-height: 1;
    color: var(--accent-red);
  }
  .abn {
    position: absolute;
    top: 22px;
    right: 24px;
    font-size: 12px;
  }
  .owner {
    position: absolute;
    left: 22px;
    top: 210px;
    color: var(--light-text);
  }
  .owner-name { font-size: 20px; font-weight: 700; }
  .owner-role { font-family: Arial, Helvetica, sans-serif; font-size: 12px; font-style: italic; }
  .contact {
    position: absolute;
    right: 24px;
    bottom: 22px;
    text-align: right;
    color: var(--light-text);
    font-size: 19px;
    line-height: 1.3;
  }
</style>
</head>
<body>
  <main class="canvas">
    <section class="card card-front">
      <div class="band band-top"></div>
      <div class="brand">
        <div class="brand-mark">
          <span class="brand-dot"></span>
          <span class="brand-name">Maison Corvel</span>
        </div>
        <p class="tagline">Cocktail Party &amp; Catering</p>
      </div>
      <div class="band band-bottom"></div>
    </section>

    <section class="card card-back">
      <p class="abn">ABN: 30918274651</p>
      <div class="brand">
        <div class="brand-mark">
          <span class="brand-dot"></span>
          <span class="brand-name">Maison Corvel</span>
        </div>
        <p class="tagline">Traditional French Food</p>
      </div>
      <div class="band band-bottom"></div>
      <div class="owner">
        <p class="owner-name">Étienne Varlin</p>
        <p class="owner-role">Owner</p>
      </div>
      <div class="contact">
        <p class="contact-email">evarlin@maisoncorvel.fr</p>
        <p class="contact-phone">0491735208</p>
      </div>
    </section>
  </main>
</body>
</html>
```